Engineering Consultant Business Card

I'm starting a new business as a high-end engineering consultant in a niche field. I've attached the jpg for my logo plus the branding guideline document that I've been following. You can see my business website here: www.tarvikworks.com
I'd like a business card that has the logo on one side, then the other side has (in any order): Tarvik Works, Inc.
Dana Whitlock
President and Chief EMC Engineer
www.tarvikworks.com
dana@tarvikworks.com
Optional: motto "We will solve your EMC problems as early as possible—ideally before they even start."
I'm not planning on including a phone number
Target Market(s)
Businesses, especially makers of electronics hardware
Industry/Entity Type
Electrical engineering
Contact Information for Business Card
Company name, my name, website, email

```html
<!DOCTYPE html>
<html lang="en">
<head>
<meta charset="utf-8">
<title>Tarvik Works – Business Card</title>
<link rel="stylesheet" href="https://fonts.googleapis.com/css2?family=Quicksand:wght@500;600;700&family=Montserrat:wght@500&display=swap">
<style>
  :root {
    --backdrop: #5b5d61;
    --card-white: #ffffff;
    --card-white-shade: #ececec;
    --brand-blue: #2c4296;
    --brand-blue-deep: #233987;
    --navy-ink: #0d1545;
    --motto-ink: #9fb8f0;
    --text-grey: #4a4a4f;
  }
  * { box-sizing: border-box; margin: 0; padding: 0; }
  html, body { width: 1200px; height: 900px; overflow: hidden; }
  body {
    background: var(--backdrop);
    font-family: "Quicksand", sans-serif;
  }
  .card-set {
    position: relative;
    width: 1200px;
    height: 900px;
  }
  .card {
    position: absolute;
    top: 170px;
    width: 320px;
    height: 560px;
    box-shadow: 0 14px 30px rgba(0,0,0,0.35);
    overflow: hidden;
  }
  .card--front {
    left: 230px;
    background: linear-gradient(160deg, var(--card-white-shade) 0%, var(--card-white) 55%);
  }
  .card--back {
    left: 650px;
    background: linear-gradient(200deg, var(--brand-blue) 0%, var(--brand-blue-deep) 100%);
  }

  /* Front */
  .brand-mark {
    position: absolute;
    left: 40px;
    top: 290px;
    display: flex;
    align-items: center;
    gap: 12px;
  }
  .brand-mark__dot {
    width: 22px;
    height: 22px;
    border-radius: 50%;
    background: var(--brand-blue);
  }
  .brand-mark__name {
    font-weight: 700;
    font-size: 26px;
    color: var(--brand-blue);
    letter-spacing: 0.5px;
  }
  .person {
    position: absolute;
    left: 40px;
    top: 384px;
  }
  .person__name {
    font-weight: 600;
    font-size: 19px;
    letter-spacing: 0.6px;
    color: var(--brand-blue);
    text-transform: uppercase;
  }
  .person__title {
    margin-top: 2px;
    font-weight: 500;
    font-size: 15.5px;
    color: var(--text-grey);
  }
  .contact-list {
    position: absolute;
    left: 40px;
    top: 466px;
    list-style: none;
  }
  .contact-list__item {
    display: flex;
    align-items: center;
    gap: 10px;
    font-weight: 500;
    font-size: 15.5px;
    color: var(--text-grey);
    line-height: 26px;
  }
  .contact-list__icon { width: 16px; height: 16px; flex: none; }

  /* Back */
  .motto {
    position: absolute;
    left: 22px;
    top: 28px;
    height: 500px;
    writing-mode: vertical-rl;
    transform: rotate(180deg);
    font-size: 10.5px;
    font-weight: 500;
    letter-spacing: 0.3px;
    color: var(--motto-ink);
    text-align: right;
  }
  .monogram {
    position: absolute;
    right: 26px;
    bottom: 22px;
    font-family: "Montserrat", sans-serif;
    font-weight: 500;
    font-size: 112px;
    line-height: 1;
    letter-spacing: -2px;
    color: var(--navy-ink);
  }
</style>
</head>
<body>
<main class="card-set">
  <section class="card card--front" aria-label="Card front">
    <div class="brand-mark">
      <span class="brand-mark__dot"></span>
      <span class="brand-mark__name">Tarvik Works</span>
    </div>
    <div class="person">
      <p class="person__name">Dana Whitlock</p>
      <p class="person__title">President and Chief EMC Engineer</p>
    </div>
    <ul class="contact-list">
      <li class="contact-list__item">
        <svg class="contact-list__icon" viewBox="0 0 16 16" aria-hidden="true">
          <rect x="1" y="3" width="14" height="10" fill="#2c4296"/>
          <path d="M1 3 L8 9 L15 3" fill="none" stroke="#fff" stroke-width="1.3"/>
        </svg>
        dana@tarvikworks.com
      </li>
      <li class="contact-list__item">
        <svg class="contact-list__icon" viewBox="0 0 16 16" aria-hidden="true">
          <g fill="none" stroke="#2c4296" stroke-width="1.2">
            <circle cx="8" cy="8" r="6.5"/>
            <ellipse cx="8" cy="8" rx="3" ry="6.5"/>
            <line x1="1.5" y1="8" x2="14.5" y2="8"/>
            <line x1="2.5" y1="4.5" x2="13.5" y2="4.5"/>
            <line x1="2.5" y1="11.5" x2="13.5" y2="11.5"/>
          </g>
        </svg>
        www.tarvikworks.com
      </li>
    </ul>
  </section>

  <section class="card card--back" aria-label="Card back">
    <p class="motto">We will solve your EMC problems as early as possible—ideally before they even start.</p>
    <p class="monogram">TWI</p>
  </section>
</main>
</body>
</html>
```